New Zealand Luggage Importer Needs Business Cards

We need professional, creative and fashionable business cards created.
We are based in New Zealand and import and distribute high-end, quality, fashionable and durable luggage.
We pride ourselves on selling the very best quality luggage, second only to 1 brand (which we won't mention here)...we use the same manufacturer. However, our prices are much more reasonable.
Industry/Entity Type
Business
Contact Information for Business Card
Mark Dunsley
027 512 4068
3/17 Harlow Street, Pinecrest Flats, Auckland, 0614
PO Box 204377, Fernside, Auckland 0731
09-528-3916
sales@brivancases.co.nz / www.brivancases.co.nz

```html
<!DOCTYPE html>
<html lang="en">
<head>
<meta charset="utf-8">
<title>Brivan Cases – Business Card</title>
<link rel="stylesheet" href="https://fonts.googleapis.com/css2?family=Signika:wght@400;600&display=swap">
<style>
  :root {
    --page: #ffffff;
    --charcoal: #363435;
    --gold-light: #f0e2a4;
    --gold-mid: #d8c47e;
    --gold-deep: #bfa95b;
    --ink: #2d2b28;
    --white: #ffffff;
    --brand-gold: #c9ad66;
  }
  * { box-sizing: border-box; margin: 0; padding: 0; }
  html, body {
    width: 1199px;
    height: 1200px;
    overflow: hidden;
    background: var(--page);
  }
  .canvas {
    position: relative;
    width: 1199px;
    height: 1200px;
    font-family: "Signika", sans-serif;
  }
  .card {
    position: absolute;
    left: 221px;
    width: 754px;
    height: 471px;
  }
  .card-front {
    top: 101px;
    background: var(--charcoal);
    display: flex;
    align-items: center;
    justify-content: center;
  }
  .card-back {
    top: 624px;
    background: radial-gradient(ellipse 60% 70% at 55% 45%, var(--gold-light) 0%, var(--gold-mid) 45%, var(--gold-deep) 100%);
  }
  .wordmark {
    font-family: "Signika", sans-serif;
    font-weight: 600;
    letter-spacing: 0.08em;
    white-space: nowrap;
    line-height: 1;
  }
  .card-front .wordmark {
    color: var(--brand-gold);
    font-size: 56px;
    margin-top: -18px;
  }
  .logo-plate {
    position: absolute;
    left: 56px;
    top: 30px;
    width: 638px;
    height: 96px;
    background: var(--white);
    border-radius: 16px;
    display: flex;
    align-items: center;
    justify-content: center;
  }
  .logo-plate .wordmark {
    color: var(--ink);
    font-size: 54px;
  }
  .contact {
    position: absolute;
    left: 42px;
    top: 148px;
    color: var(--ink);
  }
  .contact-name {
    font-style: italic;
    font-weight: 600;
    font-size: 37px;
    line-height: 44px;
    margin-bottom: 2px;
  }
  .contact-line {
    font-size: 25px;
    line-height: 42px;
    font-weight: 400;
  }
  .website {
    position: absolute;
    left: 0;
    right: 0;
    top: 412px;
    text-align: center;
    color: var(--white);
    font-size: 31px;
    font-weight: 400;
  }
</style>
</head>
<body>
<main class="canvas">
  <section class="card card-front" aria-label="Card front">
    <div class="wordmark">BRIVAN CASES</div>
  </section>

  <section class="card card-back" aria-label="Card back">
    <div class="logo-plate">
      <div class="wordmark">BRIVAN CASES</div>
    </div>
    <div class="contact">
      <p class="contact-name">Mark Dunsley</p>
      <p class="contact-line">027 512 4068</p>
      <p class="contact-line">3/17 Harlow Street, Pinecrest Flats, Auckland, 0614</p>
      <p class="contact-line">PO Box 204377, Fernside, Auckland 0731</p>
      <p class="contact-line">09-528-3916</p>
      <p class="contact-line">sales@brivancases.co.nz</p>
    </div>
    <p class="website">www.brivancases.co.nz</p>
  </section>
</main>
</body>
</html>
```